Empower our Electric Journey on the Web

We need a new website that can promote our services. Our three services that we offer are:
- Management of e-mobility charging stations
- Management of energy purchases
- Leasing of E-Mobility charging stations
- Energy billing of private electricity meters
The website should work responsively on PC, tablet and smartphone. In general, a simple navigation and an appealing design should be in the foreground. The website should give the customer the possibility to request , based pm a preset chexkbox chart and to get in contact with us.
Our logo works on black and white background.
Our slogan is:
Empower Your Electric Journey with Velmor Mobility
The 4 Pages should be the following:
Main Page, with info about us, why choose us,
2nd; services; what we sell and what are our services
3rd; Contact us, request an offer
4th, References about costumers and Work we already did, in the future we would like to integrate a Blog Post in this section in stead of references.

Target Market(s)

Landlords, Homeowners, Homeowner Associations

Industry/Entity Type

EV Chargers / E-Mobility

Coding

Coded - Design and coding required

Number of Pages Required

4 page

Requirements
Nice to have
• Pop up to our mailchimp newsletter subscription

```html
<!DOCTYPE html>
<html lang="en">
<head>
<meta charset="utf-8">
<title>Velmor Mobility – Home</title>
<link rel="stylesheet" href="https://fonts.googleapis.com/css2?family=Michroma&family=Inter:wght@400;500;600;700&display=swap">
<style>
:root{
  --green:#4cc13c;
  --green-light:#7ee04a;
  --green-dark:#2fa52f;
  --ink:#111111;
  --text:#555555;
  --grey-bg:#f3f3f3;
  --stage:#f1f8f6;
  --white:#ffffff;
  --head:'Michroma',sans-serif;
  --body:'Inter',sans-serif;
}
*{box-sizing:border-box;margin:0;padding:0}
html,body{width:868px;height:1200px;overflow:hidden;background:var(--stage)}
.stage{position:absolute;left:0;top:0;width:1640px;height:2268px;transform:scale(.52927);transform-origin:0 0;background:var(--stage);font-family:var(--body)}
.page{position:absolute;top:108px;width:661px;height:2052px;background:var(--white);overflow:hidden;box-shadow:0 6px 24px rgba(0,0,0,.06)}
.page--home{left:113px}
.page--popup{left:866px}
.abs{position:absolute}

/* top bar */
.topbar{left:0;top:0;width:661px;height:24px;background:var(--ink);color:#fff;font-size:7.5px;font-weight:500}
.topbar__item{position:absolute;top:0;height:24px;display:flex;align-items:center;gap:5px}
.topbar__sep{position:absolute;left:147px;top:7px;width:1px;height:10px;background:#aaa}
.topbar__quote{position:absolute;left:463px;top:0;width:198px;height:24px;background:linear-gradient(90deg,var(--green),var(--green-light));display:flex;align-items:center;justify-content:center;font-weight:700;font-size:7.5px}

/* header */
.brand{display:flex;align-items:center;gap:7px}
.brand__mark{width:14px;height:14px;background:var(--green)}
.brand__name{font-family:var(--head);font-size:12px;line-height:1.15;letter-spacing:1.5px;color:var(--ink)}
.header__brand{left:62px;top:43px}
.nav{left:292px;top:54px;display:flex;gap:18px;font-size:8px;font-weight:700;color:var(--ink)}
.nav__link--active{color:var(--green)}

/* hero */
.hero{left:0;top:96px;width:661px;height:369px}
.hero__photo{position:absolute;inset:0;background:linear-gradient(100deg,#cfd3d0 0%,#9da27c 30%,#7e8a2f 55%,#a48a22 80%,#6a7a1e 100%)}
.hero__title{position:absolute;left:0;top:82px;width:661px;text-align:center;font-family:var(--head);font-size:19px;line-height:27px;color:#fff;text-transform:uppercase}
.btn{display:flex;align-items:center;justify-content:center;color:#fff;font-weight:700;font-size:7.5px;background:linear-gradient(90deg,var(--green),var(--green-light))}
.hero__btn{position:absolute;left:288px;top:177px;width:84px;height:26px}
.hero__chevron{position:absolute;left:0;top:272px;width:661px;height:97px}

/* section titles */
.section-title{position:absolute;left:0;width:661px;text-align:center;font-family:var(--head);font-size:19px;color:var(--ink);line-height:24px}
.section-title span{color:var(--green)}

/* about */
.about__title{left:62px;top:502px;font-family:var(--head);font-size:19px;color:var(--ink)}
.about__title span{color:var(--green)}
.about__text{left:62px;top:540px;width:228px;font-size:7.6px;line-height:14.7px;color:var(--text);text-align:justify}
.about__text p+p{margin-top:7px}
.about__btn{left:62px;top:667px;width:76px;height:27px}
.about__frame{left:321px;top:499px;width:260px;height:222px;border:2px solid var(--green)}
.about__photo{left:340px;top:480px;width:260px;height:222px;background:linear-gradient(135deg,#d9dccf 0%,#b7c0a0 40%,#6f7d3c 75%,#3f4a2a 100%)}

/* services */
.services{left:0;top:792px;width:661px;height:311px;background:var(--grey-bg)}
.service{position:absolute;top:80px;width:126px;height:183px;background:#fff;box-shadow:0 2px 6px rgba(0,0,0,.06)}
.service__photo{position:absolute;left:0;top:0;width:126px;height:110px}
.service__chevron{position:absolute;left:0;top:96px;width:126px;height:16px}
.service__name{position:absolute;left:0;top:128px;width:126px;text-align:center;font-size:7.6px;line-height:13.2px;font-weight:700;color:var(--ink);text-transform:uppercase}
.service__line{position:absolute;left:0;bottom:0;width:126px;height:2px;background:var(--green)}
.diamond{position:absolute;background:linear-gradient(135deg,var(--green),var(--green-light));transform:rotate(45deg);display:flex;align-items:center;justify-content:center}
.diamond svg{transform:rotate(-45deg)}
.service__diamond{left:56px;top:176px;width:14px;height:14px}

/* why */
.why{left:0;top:1103px;width:661px;height:328px;background:linear-gradient(90deg,var(--green) 0%,#5ccf3f 50%,var(--green-light) 100%)}
.why .section-title{color:#fff}
.reason{position:absolute;top:86px;width:168px;height:200px;background:#fff}
.reason__diamond{left:64px;top:29px;width:40px;height:40px}
.reason__title{position:absolute;left:0;top:91px;width:168px;text-align:center;font-size:8.5px;font-weight:700;color:var(--ink)}
.reason__text{position:absolute;left:12px;top:110px;width:144px;text-align:center;font-size:7.6px;line-height:14.6px;color:var(--text)}

/* blog */
.post{position:absolute;top:1544px;width:170px;height:244px}
.post__photo{position:absolute;left:0;top:0;width:170px;height:118px}
.post__card{position:absolute;left:7px;top:108px;width:156px;height:133px;background:#fff;box-shadow:0 3px 10px rgba(0,0,0,.08)}
.post__date{position:absolute;left:12px;top:10px;height:16px;padding:0 8px;border-radius:8px;background:var(--green);color:#fff;font-size:6px;font-weight:600;display:flex;align-items:center}
.post__title{position:absolute;left:12px;top:35px;width:138px;font-size:8px;line-height:13px;font-weight:700;color:var(--ink)}
.post__text{position:absolute;left:12px;top:64px;width:138px;font-size:7.6px;line-height:13.6px;color:var(--text)}
.post__link{position:absolute;left:12px;top:113px;font-size:7px;font-weight:600;color:var(--green);text-decoration:underline}

/* footer */
.footer{left:0;top:1852px;width:661px;height:200px;background:var(--ink);color:#fff}
.footer .brand__name{color:#fff}
.footer__brand{left:62px;top:80px}
.footer__col{position:absolute;top:22px}
.footer__head{font-size:8px;font-weight:700;padding-bottom:6px;position:relative}
.footer__head::after{content:"";position:absolute;left:0;top:18px;width:63px;height:2px;background:var(--green)}
.footer__list{list-style:none;margin-top:14px;font-size:7.5px;line-height:13px}
.footer__list li{margin-bottom:7.8px}
.contact-item{display:flex;gap:10px;margin-bottom:6.5px;font-size:7.5px;line-height:13px}
.contact-item__icon{flex:none;width:20px;height:20px;border-radius:50%;background:#fff;display:flex;align-items:center;justify-content:center;margin-top:3px}
.footer__rule{left:62px;top:165px;width:538px;height:1px;background:#333}
.footer__copy{left:230px;top:177px;font-size:7.5px}
.footer__social{left:527px;top:174px;display:flex;gap:4px}
.social-dot{width:15px;height:15px;border-radius:50%;border:1px solid #fff}
.social-dot--on{background:var(--green);border-color:var(--green)}

/* newsletter popup */
.dim{left:0;top:0;width:661px;height:2052px;background:rgba(0,0,0,.62)}
.popup{left:106px;top:478px;width:449px;height:312px;background:linear-gradient(100deg,var(--green) 0%,#5fd040 55%,var(--green-light) 100%)}
.popup__icon{position:absolute;left:204px;top:39px;width:40px;height:40px;border-radius:50%;border:2px solid #fff}
.popup__title{position:absolute;left:0;top:98px;width:449px;text-align:center;font-family:var(--head);font-size:17px;color:#fff}
.popup__text{position:absolute;left:60px;top:130px;width:329px;text-align:center;font-size:9.4px;line-height:16px;color:#fff}
.popup__field{position:absolute;left:40px;width:370px;height:26px;background:#fff;font-size:8px;color:var(--ink);display:flex;align-items:center;padding-left:9px}
.popup__submit{position:absolute;left:40px;top:247px;width:370px;height:27px;background:var(--ink);color:#fff;font-size:8px;font-weight:700;display:flex;align-items:center;justify-content:center}
</style>
</head>
<body>
<div class="stage">

  <!-- Home page -->
  <div class="page page--home">
    <div class="abs topbar">
      <div class="topbar__item" style="left:62px"><svg width="7" height="7" viewBox="0 0 10 10"><path d="M2 1l2 2-1 1.5c.8 1.3 1.3 1.8 2.5 2.5L7 6l2 2-1.5 1.5C4.5 9 1 5.5.5 2.5z" fill="#4cc13c"/></svg>+1 555 014 2290</div>
      <div class="topbar__sep"></div>
      <div class="topbar__item" style="left:158px"><svg width="8" height="6" viewBox="0 0 10 7"><rect width="10" height="7" fill="#4cc13c"/><path d="M0 0l5 4 5-4" stroke="#111" fill="none"/></svg>hello@velmormobility.example</div>
      <div class="topbar__quote">GET A FREE QUOTE</div>
    </div>

    <div class="abs header__brand brand"><div class="brand__mark"></div><div class="brand__name">VELMOR<br>MOBILITY</div></div>
    <nav class="abs nav"><span class="nav__link--active">HOME</span><span>ABOUT US</span><span>OUR SERVICES</span><span>RESOURCES</span><span>CONTACT US</span></nav>

    <section class="abs hero">
      <div class="hero__photo" role="img" aria-label="Electric car plugged into a charging station in an autumn park"></div>
      <h1 class="hero__title">Empower Your<br>Electric Journey with<br>Velmor Mobility</h1>
      <div class="hero__btn btn">GET STARTED</div>
      <svg class="hero__chevron" viewBox="0 0 661 97" preserveAspectRatio="none"><polygon points="0,97 330,0 661,97" fill="#4cc13c"/><polygon points="0,97 330,12 661,97" fill="#fff"/></svg>
    </section>

    <h2 class="abs about__title">ABOUT <span>US</span></h2>
    <div class="abs about__text">
      <p>Lorem ipsum dolor sit amet, consectetur adipiscing elit, sed do eiusmod tempor incididunt ut labore et dolore magna aliqua. Ut enim ad minim veniam, quis nostrud exercitation laboris nisi ut aliquip exea.</p>
      <p>Lorem ipsum dolor sit amet, consectetur adipiscing elit, sed do eiusmod tempor incididunt ut labore et dolore magna aliqua enim minim veniam.</p>
    </div>
    <div class="abs about__btn btn">LEARN MORE</div>
    <div class="abs about__frame"></div>
    <div class="abs about__photo" role="img" aria-label="Woman charging a white electric car in a sunny field"></div>

    <section class="abs services">
      <h2 class="section-title" style="top:31px">OUR <span>SERVICES</span></h2>
      <div class="service" style="left:61px"><div class="service__photo" role="img" aria-label="Row of charging stations" style="background:linear-gradient(160deg,#cfd8d6,#6d7a66 60%,#3d4a35)"></div><svg class="service__chevron" viewBox="0 0 126 16" preserveAspectRatio="none"><polygon points="0,16 63,0 126,16" fill="#4cc13c"/><polygon points="0,16 63,4 126,16" fill="#fff"/></svg><div class="service__name">Management of<br>E-Mobility Charging<br>Stations</div><div class="service__line"></div><div class="diamond service__diamond"><svg width="7" height="7" viewBox="0 0 10 10"><path d="M4 2l3 3-3 3" stroke="#fff" stroke-width="1.6" fill="none"/></svg></div></div>
      <div class="service" style="left:199px"><div class="service__photo" role="img" aria-label="Technician with a tablet at a charging unit" style="background:linear-gradient(160deg,#dfe5e8,#8aa0ab 55%,#d9822e)"></div><svg class="service__chevron" viewBox="0 0 126 16" preserveAspectRatio="none"><polygon points="0,16 63,0 126,16" fill="#4cc13c"/><polygon points="0,16 63,4 126,16" fill="#fff"/></svg><div class="service__name">Management of<br>Energy Purchases</div><div class="service__line"></div><div class="diamond service__diamond"><svg width="7" height="7" viewBox="0 0 10 10"><path d="M4 2l3 3-3 3" stroke="#fff" stroke-width="1.6" fill="none"/></svg></div></div>
      <div class="service" style="left:337px"><div class="service__photo" role="img" aria-label="Charging plug connected to a white car" style="background:linear-gradient(160deg,#ece7e0,#c9b9a2 50%,#6b8a3c)"></div><svg class="service__chevron" viewBox="0 0 126 16" preserveAspectRatio="none"><polygon points="0,16 63,0 126,16" fill="#4cc13c"/><polygon points="0,16 63,4 126,16" fill="#fff"/></svg><div class="service__name">Leasing of<br>E-Mobility Charging<br>Stations</div><div class="service__line"></div><div class="diamond service__diamond"><svg width="7" height="7" viewBox="0 0 10 10"><path d="M4 2l3 3-3 3" stroke="#fff" stroke-width="1.6" fill="none"/></svg></div></div>
      <div class="service" style="left:474px"><div class="service__photo" role="img" aria-label="Electrician checking an electricity meter" style="background:linear-gradient(160deg,#dfe6ec,#9aa6b0 50%,#c8792c)"></div><svg class="service__chevron" viewBox="0 0 126 16" preserveAspectRatio="none"><polygon points="0,16 63,0 126,16" fill="#4cc13c"/><polygon points="0,16 63,4 126,16" fill="#fff"/></svg><div class="service__name">Energy Billing of<br>Private Electricity<br>Meters</div><div class="service__line"></div><div class="diamond service__diamond"><svg width="7" height="7" viewBox="0 0 10 10"><path d="M4 2l3 3-3 3" stroke="#fff" stroke-width="1.6" fill="none"/></svg></div></div>
    </section>

    <section class="abs why">
      <h2 class="section-title" style="top:37px">WHY CHOOSE US</h2>
      <div class="reason" style="left:61px"><div class="diamond reason__diamond"><svg width="20" height="20" viewBox="0 0 20 20"><path d="M11 2L5 11h5l-1 7 6-9h-5z" stroke="#fff" stroke-width="1.3" fill="none" stroke-linejoin="round"/></svg></div><div class="reason__title">LOREM IPSUM DOLOR</div><p class="reason__text">Lorem ipsum dolor sit amet, conse ctetur adipiscing elit, sed do ei usmod tempor incididunt ut labore et dolore magna aliqua ut enim ad minimea.</p></div>
      <div class="reason" style="left:247px"><div class="diamond reason__diamond"><svg width="20" height="20" viewBox="0 0 20 20"><rect x="3" y="8" width="14" height="6" rx="2" stroke="#fff" stroke-width="1.3" fill="none"/><circle cx="6.5" cy="15" r="1.5" fill="#fff"/><circle cx="13.5" cy="15" r="1.5" fill="#fff"/><path d="M6 8l2-3h4l2 3" stroke="#fff" stroke-width="1.3" fill="none"/></svg></div><div class="reason__title">LOREM IPSUM DOLOR</div><p class="reason__text">Lorem ipsum dolor sit amet, conse ctetur adipiscing elit, sed do ei usmod tempor incididunt ut labore et dolore magna aliqua ut enim ad minimea.</p></div>
      <div class="reason" style="left:432px"><div class="diamond reason__diamond"><svg width="20" height="20" viewBox="0 0 20 20"><circle cx="10" cy="9" r="6" stroke="#fff" stroke-width="1.3" fill="none"/><path d="M8 5v3M12 5v3M10 15v3" stroke="#fff" stroke-width="1.3"/></svg></div><div class="reason__title">LOREM IPSUM DOLOR</div><p class="reason__text">Lorem ipsum dolor sit amet, conse ctetur adipiscing elit, sed do ei usmod tempor incididunt ut labore et dolore magna aliqua ut enim ad minimea.</p></div>
    </section>

    <h2 class="section-title" style="top:1496px">LATEST <span>BLOG</span></h2>
    <article class="post" style="left:61px"><div class="post__photo" role="img" aria-label="White cars at chargers in front of a townhouse" style="background:linear-gradient(180deg,#d7d9d4,#5e7a4a 55%,#c8cbc6)"></div><div class="post__card"><span class="post__date">14 SEP 2023</span><h3 class="post__title">LOREM IPSUM DOLOR SIT AM CONSECTETUR</h3><p class="post__text">Lorem ipsum dolor sit amet.cons ctetur adipiscing elit, sed do ei usmod temporea.</p><span class="post__link">LEARN MORE</span></div></article>
    <article class="post" style="left:246px"><div class="post__photo" role="img" aria-label="Charging connectors lined up at a station" style="background:linear-gradient(160deg,#cfd8e0,#6c8ba0 50%,#c9782f)"></div><div class="post__card"><span class="post__date">14 SEP 2023</span><h3 class="post__title">LOREM IPSUM DOLOR SIT AM CONSECTETUR</h3><p class="post__text">Lorem ipsum dolor sit amet.cons ctetur adipiscing elit, sed do ei usmod temporea.</p><span class="post__link">LEARN MORE</span></div></article>
    <article class="post" style="left:430px"><div class="post__photo" role="img" aria-label="Hand plugging a charger into a car at sunset" style="background:linear-gradient(160deg,#e8d9a8,#a6893e 50%,#3b3a2e)"></div><div class="post__card"><span class="post__date">14 SEP 2023</span><h3 class="post__title">LOREM IPSUM DOLOR SIT AM CONSECTETUR</h3><p class="post__text">Lorem ipsum dolor sit amet.cons ctetur adipiscing elit, sed do ei usmod temporea.</p><span class="post__link">LEARN MORE</span></div></article>

    <footer class="abs footer">
      <div class="abs footer__brand brand"><div class="brand__mark"></div><div class="brand__name">VELMOR<br>MOBILITY</div></div>
      <div class="footer__col" style="left:235px"><div class="footer__head">CONTACT US</div>
        <div style="margin-top:14px">
          <div class="contact-item"><span class="contact-item__icon"><svg width="8" height="10" viewBox="0 0 8 10"><path d="M4 10C1 6 0 4.5 0 3.5a4 4 0 018 0C8 4.5 7 6 4 10z" fill="#4cc13c"/><circle cx="4" cy="3.6" r="1.3" fill="#fff"/></svg></span><span>27 Meadow Lane, Springfield,<br>United States</span></div>
          <div class="contact-item"><span class="contact-item__icon"><svg width="8" height="8" viewBox="0 0 10 10"><path d="M2 1l2 2-1 1.5c.8 1.3 1.3 1.8 2.5 2.5L7 6l2 2-1.5 1.5C4.5 9 1 5.5.5 2.5z" fill="#4cc13c"/></svg></span><span>Call Us:<br>+1 555 014 2290</span></div>
          <div class="contact-item"><span class="contact-item__icon"><svg width="9" height="7" viewBox="0 0 10 7"><rect width="10" height="7" fill="#4cc13c"/><path d="M0 0l5 4 5-4" stroke="#fff" fill="none"/></svg></span><span>Email Us:<br>hello@velmormobility.example</span></div>
        </div>
      </div>
      <div class="footer__col" style="left:413px"><div class="footer__head">NAVIGATION</div><ul class="footer__list"><li>Home</li><li>About Us</li><li>Our Services</li><li>Resources</li><li>Contact Us</li></ul></div>
      <div class="footer__col" style="left:525px"><div class="footer__head">QUICK LINKS</div><ul class="footer__list"><li>FAQ</li><li>Site Map</li><li>Privacy Policy</li><li>Terms Of Conditions</li></ul></div>
      <div class="abs footer__rule"></div>
      <div class="abs footer__copy">Copyright © 2023 VELMOR MOBILITY - All Rights Reserved.</div>
      <div class="abs footer__social"><span class="social-dot social-dot--on"></span><span class="social-dot"></span><span class="social-dot"></span><span class="social-dot"></span></div>
    </footer>
  </div>

  <!-- Home page with newsletter popup -->
  <div class="page page--popup">
    <div class="abs topbar">
      <div class="topbar__item" style="left:62px"><svg width="7" height="7" viewBox="0 0 10 10"><path d="M2 1l2 2-1 1.5c.8 1.3 1.3 1.8 2.5 2.5L7 6l2 2-1.5 1.5C4.5 9 1 5.5.5 2.5z" fill="#4cc13c"/></svg>+1 555 014 2290</div>
      <div class="topbar__sep"></div>
      <div class="topbar__item" style="left:158px"><svg width="8" height="6" viewBox="0 0 10 7"><rect width="10" height="7" fill="#4cc13c"/><path d="M0 0l5 4 5-4" stroke="#111" fill="none"/></svg>hello@velmormobility.example</div>
      <div class="topbar__quote">GET A FREE QUOTE</div>
    </div>

    <div class="abs header__brand brand"><div class="brand__mark"></div><div class="brand__name">VELMOR<br>MOBILITY</div></div>
    <nav class="abs nav"><span class="nav__link--active">HOME</span><span>ABOUT US</span><span>OUR SERVICES</span><span>RESOURCES</span><span>CONTACT US</span></nav>

    <section class="abs hero">
      <div class="hero__photo" role="img" aria-label="Electric car plugged into a charging station in an autumn park"></div>
      <h1 class="hero__title">Empower Your<br>Electric Journey with<br>Velmor Mobility</h1>
      <div class="hero__btn btn">GET STARTED</div>
      <svg class="hero__chevron" viewBox="0 0 661 97" preserveAspectRatio="none"><polygon points="0,97 330,0 661,97" fill="#4cc13c"/><polygon points="0,97 330,12 661,97" fill="#fff"/></svg>
    </section>

    <h2 class="abs about__title">ABOUT <span>US</span></h2>
    <div class="abs about__text">
      <p>Lorem ipsum dolor sit amet, consectetur adipiscing elit, sed do eiusmod tempor incididunt ut labore et dolore magna aliqua. Ut enim ad minim veniam, quis nostrud exercitation laboris nisi ut aliquip exea.</p>
      <p>Lorem ipsum dolor sit amet, consectetur adipiscing elit, sed do eiusmod tempor incididunt ut labore et dolore magna aliqua enim minim veniam.</p>
    </div>
    <div class="abs about__btn btn">LEARN MORE</div>
    <div class="abs about__frame"></div>
    <div class="abs about__photo" role="img" aria-label="Woman charging a white electric car in a sunny field"></div>

    <section class="abs services">
      <h2 class="section-title" style="top:31px">OUR <span>SERVICES</span></h2>
      <div class="service" style="left:61px"><div class="service__photo" role="img" aria-label="Row of charging stations" style="background:linear-gradient(160deg,#cfd8d6,#6d7a66 60%,#3d4a35)"></div><svg class="service__chevron" viewBox="0 0 126 16" preserveAspectRatio="none"><polygon points="0,16 63,0 126,16" fill="#4cc13c"/><polygon points="0,16 63,4 126,16" fill="#fff"/></svg><div class="service__name">Management of<br>E-Mobility Charging<br>Stations</div><div class="service__line"></div><div class="diamond service__diamond"></div></div>
      <div class="service" style="left:199px"><div class="service__photo" role="img" aria-label="Technician with a tablet at a charging unit" style="background:linear-gradient(160deg,#dfe5e8,#8aa0ab 55%,#d9822e)"></div><svg class="service__chevron" viewBox="0 0 126 16" preserveAspectRatio="none"><polygon points="0,16 63,0 126,16" fill="#4cc13c"/><polygon points="0,16 63,4 126,16" fill="#fff"/></svg><div class="service__name">Management of<br>Energy Purchases</div><div class="service__line"></div><div class="diamond service__diamond"></div></div>
      <div class="service" style="left:337px"><div class="service__photo" role="img" aria-label="Charging plug connected to a white car" style="background:linear-gradient(160deg,#ece7e0,#c9b9a2 50%,#6b8a3c)"></div><svg class="service__chevron" viewBox="0 0 126 16" preserveAspectRatio="none"><polygon points="0,16 63,0 126,16" fill="#4cc13c"/><polygon points="0,16 63,4 126,16" fill="#fff"/></svg><div class="service__name">Leasing of<br>E-Mobility Charging<br>Stations</div><div class="service__line"></div><div class="diamond service__diamond"></div></div>
      <div class="service" style="left:474px"><div class="service__photo" role="img" aria-label="Electrician checking an electricity meter" style="background:linear-gradient(160deg,#dfe6ec,#9aa6b0 50%,#c8792c)"></div><svg class="service__chevron" viewBox="0 0 126 16" preserveAspectRatio="none"><polygon points="0,16 63,0 126,16" fill="#4cc13c"/><polygon points="0,16 63,4 126,16" fill="#fff"/></svg><div class="service__name">Energy Billing of<br>Private Electricity<br>Meters</div><div class="service__line"></div><div class="diamond service__diamond"></div></div>
    </section>

    <section class="abs why">
      <h2 class="section-title" style="top:37px">WHY CHOOSE US</h2>
      <div class="reason" style="left:61px"><div class="diamond reason__diamond"></div><div class="reason__title">LOREM IPSUM DOLOR</div><p class="reason__text">Lorem ipsum dolor sit amet, conse ctetur adipiscing elit, sed do ei usmod tempor incididunt ut labore et dolore magna aliqua ut enim ad minimea.</p></div>
      <div class="reason" style="left:247px"><div class="diamond reason__diamond"></div><div class="reason__title">LOREM IPSUM DOLOR</div><p class="reason__text">Lorem ipsum dolor sit amet, conse ctetur adipiscing elit, sed do ei usmod tempor incididunt ut labore et dolore magna aliqua ut enim ad minimea.</p></div>
      <div class="reason" style="left:432px"><div class="diamond reason__diamond"></div><div class="reason__title">LOREM IPSUM DOLOR</div><p class="reason__text">Lorem ipsum dolor sit amet, conse ctetur adipiscing elit, sed do ei usmod tempor incididunt ut labore et dolore magna aliqua ut enim ad minimea.</p></div>
    </section>

    <h2 class="section-title" style="top:1496px">LATEST <span>BLOG</span></h2>
    <article class="post" style="left:61px"><div class="post__photo" role="img" aria-label="White cars at chargers in front of a townhouse" style="background:linear-gradient(180deg,#d7d9d4,#5e7a4a 55%,#c8cbc6)"></div><div class="post__card"><span class="post__date">14 SEP 2023</span><h3 class="post__title">LOREM IPSUM DOLOR SIT AM CONSECTETUR</h3><p class="post__text">Lorem ipsum dolor sit amet.cons ctetur adipiscing elit, sed do ei usmod temporea.</p><span class="post__link">LEARN MORE</span></div></article>
    <article class="post" style="left:246px"><div class="post__photo" role="img" aria-label="Charging connectors lined up at a station" style="background:linear-gradient(160deg,#cfd8e0,#6c8ba0 50%,#c9782f)"></div><div class="post__card"><span class="post__date">14 SEP 2023</span><h3 class="post__title">LOREM IPSUM DOLOR SIT AM CONSECTETUR</h3><p class="post__text">Lorem ipsum dolor sit amet.cons ctetur adipiscing elit, sed do ei usmod temporea.</p><span class="post__link">LEARN MORE</span></div></article>
    <article class="post" style="left:430px"><div class="post__photo" role="img" aria-label="Hand plugging a charger into a car at sunset" style="background:linear-gradient(160deg,#e8d9a8,#a6893e 50%,#3b3a2e)"></div><div class="post__card"><span class="post__date">14 SEP 2023</span><h3 class="post__title">LOREM IPSUM DOLOR SIT AM CONSECTETUR</h3><p class="post__text">Lorem ipsum dolor sit amet.cons ctetur adipiscing elit, sed do ei usmod temporea.</p><span class="post__link">LEARN MORE</span></div></article>

    <footer class="abs footer">
      <div class="abs footer__brand brand"><div class="brand__mark"></div><div class="brand__name">VELMOR<br>MOBILITY</div></div>
      <div class="footer__col" style="left:235px"><div class="footer__head">CONTACT US</div>
        <div style="margin-top:14px">
          <div class="contact-item"><span class="contact-item__icon"></span><span>27 Meadow Lane, Springfield,<br>United States</span></div>
          <div class="contact-item"><span class="contact-item__icon"></span><span>Call Us:<br>+1 555 014 2290</span></div>
          <div class="contact-item"><span class="contact-item__icon"></span><span>Email Us:<br>hello@velmormobility.example</span></div>
        </div>
      </div>
      <div class="footer__col" style="left:413px"><div class="footer__head">NAVIGATION</div><ul class="footer__list"><li>Home</li><li>About Us</li><li>Our Services</li><li>Resources</li><li>Contact Us</li></ul></div>
      <div class="footer__col" style="left:525px"><div class="footer__head">QUICK LINKS</div><ul class="footer__list"><li>FAQ</li><li>Site Map</li><li>Privacy Policy</li><li>Terms Of Conditions</li></ul></div>
      <div class="abs footer__rule"></div>
      <div class="abs footer__copy">Copyright © 2023 VELMOR MOBILITY - All Rights Reserved.</div>
      <div class="abs footer__social"><span class="social-dot social-dot--on"></span><span class="social-dot"></span><span class="social-dot"></span><span class="social-dot"></span></div>
    </footer>

    <div class="abs dim"></div>

    <div class="abs popup" role="dialog" aria-label="Newsletter signup">
      <div class="popup__icon"></div>
      <h2 class="popup__title">JOIN OUR NEWSLETTER</h2>
      <p class="popup__text">Lorem ipsum dolor sit amet, consectetur adipiscing elit, sed do eiusmod dolore magna aliqua.</p>
      <div class="popup__field" style="top:177px">Your Name</div>
      <div class="popup__field" style="top:210px">Your Em,ail</div>
      <div class="popup__submit">SUBSCRIBE</div>
    </div>
  </div>

</div>
</body>
</html>
```